RLW CONSTRUCTION CO POSTCARD DESIGN

I was thinking of making a postcard for mailings by printmoor and or by me dropping off at homes . I guess it would be used as a mailing post card and or flyer . I have had sketch harbor design my buisnes cards . The buisness card design is a different version from my signage on trucks because of space . I have a logo design . thyat i can upload . I like silver for back ground and black for logo and letters with glossy finish . I would like to have the RLW with a back drop to give it depth , it would be the same color as windows .

The file i submitted ha a design with red letters , this design is more detailed than the other and should be used . The colors should be black on a silver card glossy . The windows and maybe give the letters depth with a backdrop outline . I want to let home owners know that they can always call for consultation and and repairs or maintenance for their home .

Target Market(s)

home owners

Industry/Entity Type

Construction

Other font styles liked:
• The same font as used in the picture of the sign i uploaded

Requirements
Must have
• HOME IMPROVEMENTS , MAINTENANCE AND REPAIRS , CARPENTRY , TILE PAINTING ECT

```html
<!DOCTYPE html>
<html lang="en">
<head>
<meta charset="utf-8">
<title>RLW Construction Co. Postcard</title>
<link rel="stylesheet" href="https://fonts.googleapis.com/css2?family=Open+Sans:wdth,wght@75,300;75,400;75,600;75,700&family=Tinos:wght@400&family=Cormorant+Garamond:ital,wght@1,500&display=swap">
<style>
  :root {
    --page-bg: #8a7a70;
    --card-silver-light: #f6f6f6;
    --card-silver: #dcdcdc;
    --card-silver-dark: #bdbdbd;
    --ink: #111111;
    --ink-soft: #333333;
    --accent-red: #e0141b;
    --photo-green: #5d7a3e;
    --photo-sky: #e9eef0;
    --photo-house: #c9b59a;
    --photo-warm: #f1dc9a;
    --photo-toy: #2f5a3c;
  }
  * { box-sizing: border-box; margin: 0; padding: 0; }
  html, body { width: 1200px; height: 1000px; overflow: hidden; }
  body {
    background: var(--page-bg);
    position: relative;
    font-family: "Open Sans", "Arial Narrow", sans-serif;
    font-stretch: 75%;
    color: var(--ink);
  }

  .card {
    position: absolute;
    overflow: hidden;
    box-shadow: 0 8px 24px rgba(0,0,0,0.35);
  }

  /* ---------- Front ---------- */
  .card--front {
    left: 60px; top: 50px; width: 620px; height: 440px;
    background: linear-gradient(135deg, var(--card-silver-light) 0%, var(--card-silver) 55%, var(--card-silver-dark) 100%);
  }
  .front__photo {
    position: absolute; left: 230px; top: 70px; width: 390px; height: 310px;
    background:
      radial-gradient(ellipse at 50% 35%, var(--photo-house) 0%, rgba(201,181,154,0.6) 30%, transparent 55%),
      linear-gradient(180deg, var(--photo-sky) 0%, #b7c3a5 45%, var(--photo-green) 80%, #a7b08c 100%);
    -webkit-mask-image: radial-gradient(ellipse at 60% 50%, #000 55%, transparent 78%);
            mask-image: radial-gradient(ellipse at 60% 50%, #000 55%, transparent 78%);
  }
  .front__headline {
    position: absolute; left: 250px; top: 16px;
    font-family: "Cormorant Garamond", "Times New Roman", serif;
    font-style: italic; font-weight: 500; font-stretch: normal;
    font-size: 30px; line-height: 1.15; color: var(--ink);
  }
  .front__headline span { display: block; }
  .front__headline span + span { padding-left: 90px; }

  .brand { display: flex; align-items: center; gap: 8px; }
  .brand__square { width: 22px; height: 22px; background: var(--ink); flex: none; }
  .brand__name {
    font-weight: 700; color: var(--ink); letter-spacing: 1px; white-space: nowrap;
  }
  .front__brand { position: absolute; left: 44px; top: 110px; }
  .front__brand .brand__name { font-size: 46px; line-height: 1; }

  .front__services {
    position: absolute; left: 44px; top: 182px;
    list-style: none;
    font-weight: 400; font-size: 21px; line-height: 1.15; text-transform: uppercase;
    color: var(--ink);
  }
  .front__cta { position: absolute; left: 44px; top: 345px; }
  .cta__label { font-weight: 700; font-size: 34px; line-height: 1; white-space: nowrap; }
  .cta__phone { font-weight: 400; font-size: 32px; line-height: 1.1; white-space: nowrap; }
  .front__contact {
    position: absolute; left: 300px; top: 378px;
    font-style: normal;
    font-weight: 400; font-size: 14px; line-height: 1.4; color: var(--ink-soft);
    white-space: nowrap;
  }

  /* ---------- Back ---------- */
  .card--back {
    left: 560px; top: 530px; width: 580px; height: 440px;
    background: linear-gradient(160deg, #ffffff 0%, var(--card-silver-light) 45%, var(--card-silver) 100%);
  }
  .back__photo {
    position: absolute; left: 250px; top: 100px; width: 330px; height: 340px;
    background:
      radial-gradient(ellipse at 55% 45%, var(--photo-toy) 0%, rgba(47,90,60,0.8) 22%, transparent 40%),
      radial-gradient(ellipse at 55% 25%, #e9a58c 0%, transparent 30%),
      linear-gradient(180deg, #fbf3d2 0%, var(--photo-warm) 50%, #9b8a6a 100%);
    -webkit-mask-image: linear-gradient(90deg, transparent 0%, #000 22%);
            mask-image: linear-gradient(90deg, transparent 0%, #000 22%);
  }
  .back__brand { position: absolute; left: 36px; top: 70px; }
  .back__brand .brand__square { width: 18px; height: 18px; }
  .back__brand .brand__name { font-size: 22px; line-height: 1; letter-spacing: 0.5px; }
  .back__reg {
    position: absolute; left: 62px; top: 98px;
    font-weight: 400; font-size: 13px; color: var(--ink-soft); white-space: nowrap;
  }
  .back__cta { position: absolute; right: 68px; top: 36px; }
  .back__cta .cta__label { font-size: 32px; }
  .back__cta .cta__phone { font-size: 30px; }
  .back__copy {
    position: absolute; left: 24px; top: 140px; width: 250px;
    font-family: "Tinos", "Times New Roman", serif; font-stretch: normal;
    font-size: 15px; line-height: 1.27; color: var(--ink);
  }
  .back__tagline {
    position: absolute; left: 24px; top: 340px; width: 230px;
    font-family: "Tinos", "Times New Roman", serif; font-stretch: normal;
    font-size: 19px; line-height: 1.2; color: var(--accent-red);
  }
</style>
</head>
<body>

<section class="card card--front" aria-label="Postcard front">
  <div class="front__photo" role="img" aria-label="Photograph of a two-storey family home with porch, garden beds and front steps"></div>

  <h1 class="front__headline"><span>Maintaining and</span><span>Enhancing your Home</span></h1>

  <div class="brand front__brand">
    <span class="brand__square"></span>
    <span class="brand__name">RLW</span>
  </div>

  <ul class="front__services">
    <li>Construction,</li>
    <li>Home Improvements ,</li>
    <li>Carpentry ,</li>
    <li>Tile, Painting,</li>
    <li>Maintenance and</li>
    <li>Repairs Ect</li>
  </ul>

  <div class="front__cta">
    <p class="cta__label">Call Us Now</p>
    <p class="cta__phone">555-201-4386</p>
  </div>

  <address class="front__contact">
    R L W Construction Co. 112 Alder Lane Northfield, MA 02190<br>
    www.rlwconstructionco.com
  </address>
</section>

<section class="card card--back" aria-label="Postcard back">
  <div class="back__photo" role="img" aria-label="Photograph of a small green model house with a pink roof resting on coins"></div>

  <div class="brand back__brand">
    <span class="brand__square"></span>
    <span class="brand__name">RLW CONSTRUCTION CO.</span>
  </div>
  <p class="back__reg">Home improvement Reg# 408317</p>

  <div class="back__cta">
    <p class="cta__label">Call Us Now</p>
    <p class="cta__phone">555-201-4386</p>
  </div>

  <p class="back__copy">The success of a new construction project depends on the talent and dedication of the tradespeople whose job it is to bring the project to life. R L W Construction Co. has a clear mission that's been driving its success - and the success of its clients - for years. Our goals can be summed up in one simple statement:</p>

  <p class="back__tagline">Flexibility, Innovation &amp; Results - for a Lasting Partnership</p>
</section>

</body>
</html>
```